Business Card/Email Signature design

We need an new business card design for our business as well as an animated email signature design.<br/>Business Card:<br/>The business card designs need to have the following information for each director:<br/>Leon Bramwell<br/>Managing Director<br/>leon@talvoraworks.com.au<br/>0498617340<br/>www.talvoraworks.com.au<br/><br/>and<br/><br/>Priscilla Venton<br/>Director<br/>priscilla@talvoraworks.com.au<br/>0467302958<br/>www.talvoraworks.com.au<br/><br/>I will upload the Talvora. Works logo designs to be used for the design. Our colours are black and white. I would like to see the designs in both coloured backgrounds.<br/><br/>For the email signature we need the same information. I also need to add a logo of our association BLPX of which i will add the logo as well. This BLPX logo does not need to be used for the business card unless it works with the design.<br/>For the animation part of the logo our company is called Talvora. Works - We have a number of divisions called Talvora. Construct, Talvora. Property, Talvora. Sales, Talvora. Executive Support, Talvora. Private PA, Talvora. Talent and Talvora. Coaching<br/>I would like for the email Signature to be designed so that the Talvora. stays still but the words Construct, Property, Sales, Executive Support, Private PA, Talent and Coaching rotate through to capture attention and tell the story of what we do.<br/><br/>Any questions please don't hesitate to message me.

Industry/Entity Type

Recruiter

Contact Information for Business Card

Leon Bramwell
Managing Director
leon@talvoraworks.com.au
0498617340
www.talvoraworks.com.au

Priscilla Venton
Director
priscilla@talvoraworks.com.au
0467302958
www.talvoraworks.com.au

Font styles to use
Serif

Colors

Designer to choose colors to be used in the design.

Requirements
Must have
• The animation for the email signature as described
Should not have
• Any changes to my logo. Any colour other that black or white

```html
<!DOCTYPE html>
<html lang="en">
<head>
<meta charset="utf-8">
<title>Talvora. Works – Business Card</title>
<link rel="stylesheet" href="https://fonts.googleapis.com/css2?family=Merriweather:wght@700&family=Noto+Serif:wght@400&display=swap">
<style>
  :root {
    --backdrop: #9c9c9c;
    --card: #0b0b0b;
    --ink: #f2f2f2;
    --ink-soft: #d9d9d9;
    --rule: #cfcfcf;
  }
  * { box-sizing: border-box; margin: 0; padding: 0; }
  html, body {
    width: 1200px;
    height: 720px;
    overflow: hidden;
    background: var(--backdrop);
  }
  .canvas {
    position: relative;
    width: 1200px;
    height: 720px;
    display: flex;
    align-items: center;
    justify-content: center;
    gap: 40px;
  }
  .card {
    position: relative;
    width: 540px;
    height: 330px;
    background: var(--card);
    color: var(--ink);
    font-family: "Noto Serif", Georgia, serif;
    box-shadow: 0 6px 18px rgba(0, 0, 0, 0.35);
    overflow: hidden;
  }

  /* Front: wordmark */
  .wordmark {
    position: absolute;
    left: 50%;
    top: 50%;
    transform: translate(-50%, -50%);
    display: flex;
    align-items: center;
    gap: 16px;
  }
  .wordmark-square {
    width: 18px;
    height: 18px;
    background: var(--ink);
  }
  .wordmark-name {
    font-size: 40px;
    letter-spacing: 0.04em;
    color: var(--ink);
    white-space: nowrap;
  }

  /* Back: contact side */
  .person {
    position: absolute;
    left: 44px;
    top: 44px;
  }
  .person-name {
    font-family: "Merriweather", Georgia, serif;
    font-weight: 700;
    font-size: 20px;
    letter-spacing: 0.01em;
  }
  .person-title {
    margin-top: 4px;
    font-size: 14px;
    color: var(--ink-soft);
  }
  .person-rule {
    position: absolute;
    left: 0;
    top: 104px;
    width: 300px;
    height: 1px;
    background: var(--rule);
  }
  .contact {
    position: absolute;
    left: 238px;
    bottom: 40px;
    list-style: none;
    font-size: 15px;
    line-height: 1.55;
    color: var(--ink);
  }
</style>
</head>
<body>
  <main class="canvas">
    <section class="card card-front" aria-label="Card front">
      <div class="wordmark">
        <span class="wordmark-square" aria-hidden="true"></span>
        <span class="wordmark-name">Talvora. Works</span>
      </div>
    </section>

    <section class="card card-back" aria-label="Card back">
      <div class="person">
        <p class="person-name">Leon Bramwell</p>
        <p class="person-title">Managing Director</p>
      </div>
      <div class="person-rule" aria-hidden="true"></div>
      <ul class="contact">
        <li>leon@talvoraworks.com.au</li>
        <li>0498617340</li>
        <li>www.talvoraworks.com.au</li>
      </ul>
    </section>
  </main>
</body>
</html>
```